Hot Consulting firm collateral upgrade

We need a stationary design for our Oakland based consulting company called Tarvulix. We provide consulting expertise in BQR compliance for Medical Device, Pharmaceutical, and Biotech companies. We will be using the stationary for all of our marketing collateral. We want the design to convey professionalism and quality. You can find our company color scheme from our website tarvulix-hq.com. I have included a copy of our current stationary that needs an upgrade.
Target Market(s)
Medical Device, Pharma, and Biotech companies
Industry/Entity Type
It Company
Look and feel

```html
<!DOCTYPE html>
<html lang="en">
<head>
<meta charset="utf-8">
<title>Tarvulix Stationery</title>
<link href="https://fonts.googleapis.com/css2?family=Questrial&display=swap" rel="stylesheet">
<style>
  :root {
    --brand-blue: #0a559f;
    --brand-blue-deep: #0b4c92;
    --paper: #f1f1f1;
    --ink: #3a3a3a;
    --ink-soft: #555;
    --stage: #d2d2d2;
    --white: #ffffff;
  }
  * { margin: 0; padding: 0; box-sizing: border-box; }
  html, body { width: 1200px; height: 1000px; overflow: hidden; }
  body {
    background: var(--stage);
    font-family: "Questrial", "Century Gothic", sans-serif;
    color: var(--ink);
    position: relative;
  }
  .piece { position: absolute; }
  .wordmark {
    font-family: "Questrial", "Century Gothic", sans-serif;
    font-weight: 400;
    letter-spacing: 0.5px;
    white-space: nowrap;
    display: flex;
    align-items: center;
    gap: 6px;
  }
  .wordmark .dot { display: inline-block; border-radius: 50%; }

  /* Presentation folder */
  .folder {
    left: 152px; top: 41px; width: 431px; height: 559px;
    background: linear-gradient(180deg, #0a57a3 0%, var(--brand-blue-deep) 100%);
    border-radius: 4px;
  }
  .folder .spine {
    position: absolute; left: 24px; top: 0; bottom: 0; width: 1px;
    background: rgba(0,0,0,0.18);
  }
  .folder .wordmark {
    position: absolute; left: 0; right: 0; top: 134px; justify-content: center;
    color: var(--white); font-size: 36px;
  }
  .folder .wordmark .dot { width: 10px; height: 10px; background: var(--white); }

  /* Letterhead */
  .letterhead {
    left: 616px; top: 61px; width: 417px; height: 539px;
    background: var(--paper);
  }
  .letterhead .masthead {
    position: absolute; left: 32px; right: 32px; top: 42px;
    display: flex; align-items: center; gap: 14px;
  }
  .letterhead .rule { flex: 1; height: 1px; background: var(--ink); }
  .letterhead .wordmark { color: var(--ink); font-size: 23px; }
  .letterhead .wordmark .dot { width: 7px; height: 7px; background: var(--brand-blue); }
  .letter-body {
    position: absolute; left: 38px; right: 38px; top: 170px;
    font-size: 5.8px; line-height: 7.2px; color: var(--ink-soft); text-align: justify;
  }
  .letter-body p { margin-bottom: 7px; }
  .letter-body .salutation { font-weight: 700; color: var(--ink); }
  .letter-body .signoff { margin-bottom: 0; }
  .letter-body .signer { font-weight: 700; color: var(--ink); }
  .signature {
    position: absolute; left: 90px; top: 342px; width: 86px; height: 40px;
    background: linear-gradient(90deg, rgba(60,80,170,0.12), rgba(60,80,170,0.22));
    border-radius: 3px;
  }
  .letter-footer {
    position: absolute; left: 0; right: 0; bottom: 0; height: 23px;
    background: var(--brand-blue); color: var(--white);
    display: flex; align-items: center; justify-content: space-between;
    padding: 0 22px; font-size: 6px;
  }
  .contact-row { display: flex; gap: 12px; align-items: center; }
  .contact-item { display: flex; align-items: center; gap: 3px; }
  .contact-item svg { width: 7px; height: 7px; }

  /* Envelope front */
  .envelope-front {
    left: 117px; top: 629px; width: 466px; height: 202px;
    background: var(--paper);
  }
  .envelope-front .wordmark {
    position: absolute; left: 27px; top: 35px; color: var(--ink); font-size: 24px;
  }
  .envelope-front .wordmark .dot { width: 7px; height: 7px; background: var(--brand-blue); }
  .envelope-front .band {
    position: absolute; left: 0; right: 0; bottom: 0; height: 23px;
    background: var(--brand-blue); color: var(--white);
    font-size: 6.5px; display: flex; align-items: center; padding-left: 16px;
  }

  /* Envelope back */
  .envelope-back {
    left: 616px; top: 629px; width: 466px; height: 202px;
    background: var(--paper);
  }
  .envelope-back svg { position: absolute; left: 0; top: 0; }

  /* Business cards */
  .card-front {
    left: 410px; top: 860px; width: 173px; height: 100px;
    background: var(--brand-blue);
  }
  .card-front .wordmark {
    position: absolute; right: 20px; top: 66px; color: var(--white); font-size: 14px; gap: 4px;
  }
  .card-front .wordmark .dot { width: 5px; height: 5px; background: var(--white); }
  .card-back {
    left: 616px; top: 860px; width: 173px; height: 100px;
    background: var(--paper);
  }
  .card-back .address {
    position: absolute; left: 10px; top: 26px; font-size: 4.6px; line-height: 5.6px; color: var(--ink-soft);
  }
  .card-back .wordmark {
    position: absolute; right: 12px; top: 24px; color: var(--ink); font-size: 15px; gap: 4px;
  }
  .card-back .wordmark .dot { width: 5px; height: 5px; background: var(--brand-blue); }
  .card-back .band {
    position: absolute; left: 0; right: 0; bottom: 0; height: 38px;
    background: var(--brand-blue); color: var(--white);
  }
  .card-back .band .contacts {
    position: absolute; left: 10px; top: 9px; font-size: 4.4px; line-height: 5.6px;
  }
  .card-back .band .person {
    position: absolute; right: 10px; top: 10px; text-align: right;
  }
  .card-back .person .name { font-size: 6px; font-weight: 700; letter-spacing: 0.3px; }
  .card-back .person .role { font-size: 5px; margin-top: 2px; }
</style>
</head>
<body>

  <section class="piece folder" aria-label="Presentation folder">
    <div class="spine"></div>
    <div class="wordmark"><span>tarvulix</span><span class="dot"></span></div>
  </section>

  <section class="piece letterhead" aria-label="Letterhead">
    <header class="masthead">
      <span class="rule"></span>
      <div class="wordmark"><span>tarvulix</span><span class="dot"></span></div>
      <span class="rule"></span>
    </header>
    <div class="letter-body">
      <p class="salutation">Dear sir,</p>
      <p>Compliance is a vital part of every medical product program. Our team works alongside device, pharmaceutical and biotech makers to plan audits, review quality systems and prepare clear records. Every engagement begins with listening, so that the guidance we provide fits your process, your schedule and your goals.</p>
      <p>In a field of fast change and new rules, documentation often falls behind. We help organizations close those gaps with practical procedures, training sessions and ongoing reviews. Our consultants have guided many firms through inspections, submissions and corrective actions, and we bring that experience to each new client relationship we build.</p>
      <p>A strong quality system speaks volumes about a company. We take great care to ensure that every report, plan and recommendation is accurate, useful and easy for your staff to follow day to day.</p>
      <p>We would welcome the chance to discuss your upcoming projects. Please reach out at any time so we can arrange a short meeting and outline how our services can support your team.</p>
      <p class="signoff">Yours Sincerely,</p>
      <p class="signer">Dara Velkin</p>
    </div>
    <div class="signature" role="img" aria-label="Handwritten signature of Dara Velkin"></div>
    <footer class="letter-footer">
      <span>Bay Area HQ, 4410 Harbor Crest Avenue- Suite 820, Oakland, CA 94607</span>
      <div class="contact-row">
        <span class="contact-item">
          <svg viewBox="0 0 10 10"><rect width="10" height="10" rx="1.5" fill="#fff"/><path d="M3 2.5l1 1.6-.6.7a4 4 0 0 0 1.8 1.8l.7-.6 1.6 1-.6 1.2C4.5 8 2 5.5 1.8 3.1z" fill="#0a559f"/></svg>
          (510) 555-0142
        </span>
        <span class="contact-item">
          <svg viewBox="0 0 10 10"><rect width="10" height="10" rx="1.5" fill="#fff"/><rect x="2" y="3" width="6" height="4" fill="none" stroke="#0a559f" stroke-width="0.8"/><path d="M2 3l3 2.2L8 3" fill="none" stroke="#0a559f" stroke-width="0.8"/></svg>
          info@tarvulix-hq.com
        </span>
        <span class="contact-item">
          <svg viewBox="0 0 10 10"><rect width="10" height="10" rx="1.5" fill="#fff"/><circle cx="5" cy="5" r="2.8" fill="none" stroke="#0a559f" stroke-width="0.8"/><path d="M2.2 5h5.6M5 2.2v5.6" stroke="#0a559f" stroke-width="0.6"/></svg>
          www.tarvulix-hq.com
        </span>
      </div>
    </footer>
  </section>

  <section class="piece envelope-front" aria-label="Envelope front">
    <div class="wordmark"><span>tarvulix</span><span class="dot"></span></div>
    <div class="band">4410 Harbor Crest Avenue- Suite 820, Oakland, CA 94607</div>
  </section>

  <section class="piece envelope-back" aria-label="Envelope back">
    <svg width="466" height="202" viewBox="0 0 466 202">
      <path d="M0 0H466V6L442 78H24L0 6Z" fill="#0a559f"/>
      <circle cx="233" cy="40" r="4" fill="#ffffff"/>
    </svg>
  </section>

  <section class="piece card-front" aria-label="Business card front">
    <div class="wordmark"><span>tarvulix</span><span class="dot"></span></div>
  </section>

  <section class="piece card-back" aria-label="Business card back">
    <div class="address">Bay Area HQ<br>4410 Harbor Crest<br>Avenue<br>Oakland, CA 94607</div>
    <div class="wordmark"><span>tarvulix</span><span class="dot"></span></div>
    <div class="band">
      <div class="contacts">(510) 555-0142<br>info@tarvulix-hq.com<br>www.tarvulix-hq.com</div>
      <div class="person">
        <div class="name">RENN HALLOWAY</div>
        <div class="role">Account Executive</div>
      </div>
    </div>
  </section>

</body>
</html>
```